Twitter/Facebook Graphics
Travel Agency
Twitter/Facebook Graphics - Travel
I need Twitter background and Facebook landing page.
Travel
Modern, elegant
I need a Twitter background with logo, I would like the contact info on the left hand side to the main Twitter page. Phone: 866-413-7058 Website: www.palvantrx.com Facebook: facebook.com/palvanTRX Twitter: @palvantrx Email: gloria@palvantrx.com - - - - - - I would like a facebook landing page introducing the business, asking people to "Like" our page in order to receive updates of the launch date.

```html
<!DOCTYPE html>
<html lang="en">
<head>
<meta charset="utf-8">
<title>palvan – Page Landing Tab</title>
<link rel="stylesheet" href="https://fonts.googleapis.com/css2?family=Arimo:wght@400;700&display=swap">
<style>
:root{
  --page:#ffffff;
  --ink:#333333;
  --muted:#808080;
  --link:#3b5998;
  --rule:#d8dfea;
  --btn:#eceef5;
  --btn-edge:#cad4e7;
  --sky-top:#5b8fd0;
  --sky-mid:#a9c9ec;
  --sea:#2fb4c4;
  --sea-deep:#0f7f9a;
  --sand:#e8d9b8;
  --brand:#f28a1c;
  --white:#ffffff;
}
*{box-sizing:border-box;margin:0;padding:0}
html,body{width:1200px;height:643px;overflow:hidden;background:var(--page)}
body{position:relative;font-family:"Arimo",Arial,sans-serif;color:var(--ink);font-size:11px}
.topbar .btn{position:absolute;top:14px;height:22px;padding:0 8px;background:var(--btn);border:1px solid var(--btn-edge);font-size:11px;font-weight:700;line-height:20px;color:var(--ink)}
.topbar .like{left:462px}
.topbar .create{left:895px}

.cover{position:absolute;left:149px;top:48px;width:194px;height:432px;
  background:linear-gradient(180deg,var(--sky-top) 0%,var(--sky-mid) 45%,var(--white) 62%,var(--sea) 78%,var(--sea-deep) 100%)}
.cover .brand{position:absolute;left:18px;top:44px;font-size:38px;font-weight:700;color:var(--brand);letter-spacing:-1px}

.likes{position:absolute;left:149px;top:495px;width:180px}
.side-head{display:flex;justify-content:space-between;font-weight:700;font-size:11px;color:var(--ink);border-bottom:1px solid var(--rule);padding-bottom:3px;margin-bottom:7px}
.side-head a,.link{color:var(--link);font-weight:400;text-decoration:none}
.like-item{display:flex;gap:8px;align-items:center;margin-bottom:9px;font-size:10px}
.thumb{width:32px;height:32px;flex:none;background:linear-gradient(135deg,#c7cfdc,#8c99ad)}
.like-item b{color:var(--link)}

.tab{position:absolute;left:343px;top:60px;width:430px;height:583px;
  background:linear-gradient(180deg,var(--sky-top) 0%,var(--sky-mid) 30%,var(--sea) 52%,var(--sea-deep) 72%,var(--sand) 100%)}
.tab .arrow{position:absolute;left:118px;top:8px}
.tab .like-us{position:absolute;left:60px;top:94px;display:flex;align-items:center;gap:10px}
.tab .like-us .fbtn{background:var(--btn);border:1px solid var(--btn-edge);color:var(--link);font-weight:700;font-size:15px;padding:3px 10px}
.tab .like-us span{color:var(--white);font-size:24px}
.portrait{position:absolute;left:12px;top:156px;width:176px;height:120px;border:4px solid var(--white);
  background:linear-gradient(160deg,#b98a6a,#6b4a38 60%,#3a2a22)}
.tab h1{position:absolute;left:12px;top:296px;font-size:15px;font-weight:400;color:var(--white)}
.tab .intro{position:absolute;left:12px;top:326px;width:192px;font-size:10px;line-height:13px;color:var(--white)}
.tab .logo{position:absolute;left:20px;top:465px;font-size:92px;font-weight:700;color:var(--brand);letter-spacing:-3px}
.tab .tagline{position:absolute;left:40px;top:560px;font-size:10px;letter-spacing:4px;color:var(--muted)}

.rail{position:absolute;left:792px;top:60px;width:230px}
.rail section{margin-bottom:14px}
.row{display:flex;gap:7px;font-size:10px;line-height:13px;margin-bottom:6px}
.avatar{width:36px;height:36px;flex:none;background:linear-gradient(135deg,#d3b6a0,#7a5a48)}
.dot{width:12px;height:12px;flex:none;background:var(--link)}
.ad-title{font-weight:700;color:var(--link);font-size:10px;margin-bottom:3px}
.ad .pic{width:60px;height:56px;flex:none;background:linear-gradient(135deg,#f4f4f4,#9aa6b8)}
</style>
</head>
<body>
<header class="topbar">
  <div class="btn like">Like</div>
  <div class="btn create">Create a Page</div>
</header>

<div class="cover" role="img" aria-label="Tropical sky and turquoise sea photograph">
  <div class="brand">palvan</div>
</div>

<aside class="likes">
  <div class="side-head">Likes <a href="#">See All</a></div>
  <div class="like-item"><div class="thumb"></div><b>Verdant Active Triathlon</b></div>
  <div class="like-item"><div class="thumb"></div><b>Ukta Actorpool</b></div>
  <div class="like-item"><div class="thumb"></div><b>Ostrin Milano</b></div>
</aside>

<main class="tab" role="img" aria-label="Beach photograph with turquoise sea and a pier house">
  <svg class="arrow" width="40" height="80" viewBox="0 0 40 80"><path d="M20 80V12M6 26L20 10 34 26" fill="none" stroke="#fff" stroke-width="5"/></svg>
  <div class="like-us"><div class="fbtn">Like</div><span>Like Us</span></div>
  <div class="portrait" role="img" aria-label="Portrait of a smiling travel agent"></div>
  <h1>Lorem ipsum dolor sit amet</h1>
  <p class="intro">Nullam feugiat enim ut mauris pharetra fermentum consectetur nunc gravida. Integer tincidunt risus sit amet mauris interdum at pharetra velit mollis. Nunc dictum imperdiet lectus, eget convallis diam viverra et. Fusce eget diam lectus, in vulputate velit. Pellentesque eus.</p>
  <div class="logo">palvan</div>
  <div class="tagline">destination weddings &amp; honeymoons</div>
</main>

<aside class="rail">
  <section>
    <div class="side-head">You and Plumcrate Active</div>
    <div class="row"><div class="dot"></div><span class="link">Plumcrate</span></div>
  </section>
  <section>
    <div class="side-head">Birthdays <a href="#">See All</a></div>
    <div class="row"><div class="avatar"></div><div><span class="link">Lina Sorel</span><br>It's her birthday.<br><span class="link">Say Happy Birthday</span></div></div>
  </section>
  <section>
    <div class="side-head">Friends' Events <a href="#">See All</a></div>
    <div class="row"><div class="avatar"></div><div><span class="link">Seaside evening gathering</span><br>Friday at 9:00am until Friday at 6:00pm<br><span class="link">Yes · No · Maybe</span></div></div>
  </section>
  <section>
    <div class="side-head">Sponsored <a href="#">Create an Ad</a></div>
    <div class="ad">
      <div class="ad-title">Do you have an Oldline PBX?</div>
      <div class="row"><div class="pic"></div><div>callvane.com<br>Don't be forced into buying another proprietary PBX. Download Callvane, an open standard SIP phone system.</div></div>
    </div>
    <div class="ad">
      <div class="ad-title">Stylenook</div>
      <div class="row"><div class="pic"></div><div>Click 'Like' if you think you can make her dress your own.<br><span class="link">Like</span> · Tia Morel and Ana Vell like this.</div></div>
    </div>
    <div class="ad">
      <div class="ad-title">Project Manager Wanted</div>
      <div class="row"><div class="pic"></div><div>Project Manager needed in your area now!</div></div>
    </div>
  </section>
</aside>
</body>
</html>
```